DJ Marcus Tevane

I'm looking for a professional but still artsy/progressive design. I come from a hip hop/club DJ background playing a lot of underground music but have switched to doing more corporate parties and weddings recently. I am all about keeping the dancefloor moving and emotionally connecting with the crowd. I'd like a trendy/updated color palette. Something that's clean enough that looks professional but also trendy enough to convey that by the end of the night we'll be sweatily dancing to the latest hits. Some designers/artists I like: Rolo Pemberack, Gavin Struthe, Dorian Fellick, Orbitex 3100, Wade Ipsley.

```html
<!DOCTYPE html>
<html lang="en">
<head>
<meta charset="utf-8">
<title>DJ Marcus Tevane – Business Card</title>
<link rel="stylesheet" href="https://fonts.googleapis.com/css2?family=Oswald:wght@500&family=Roboto:wght@400;700&display=swap">
<style>
  :root {
    --card-black: #0b0608;
    --name-yellow: #ffe600;
    --contact-white: #ffffff;
    --splash-red: #b8241c;
    --splash-yellow: #f5d31a;
    --splash-blue: #2a3aa8;
    --splash-white: #e8eef6;
  }
  html, body {
    margin: 0;
    padding: 0;
    width: 1200px;
    height: 702px;
    overflow: hidden;
    background: var(--card-black);
  }
  .card {
    position: relative;
    width: 1200px;
    height: 702px;
    background: var(--card-black);
    overflow: hidden;
  }
  .card__art {
    position: absolute;
    left: 330px;
    top: 0;
    width: 870px;
    height: 702px;
  }
  .card__name {
    position: absolute;
    left: 76px;
    top: 78px;
    margin: 0;
    font-family: "Oswald", "Arial Narrow", sans-serif;
    font-weight: 500;
    font-size: 70px;
    line-height: 86px;
    color: var(--name-yellow);
    text-transform: uppercase;
    letter-spacing: 0.5px;
  }
  .card__name span { display: block; }
  .card__contact {
    position: absolute;
    left: 78px;
    top: 486px;
    margin: 0;
    font-family: "Roboto", Arial, sans-serif;
    color: var(--contact-white);
    font-style: normal;
  }
  .contact__phone {
    display: block;
    font-weight: 700;
    font-size: 34px;
    line-height: 46px;
    letter-spacing: 0.5px;
  }
  .contact__line {
    display: block;
    font-weight: 400;
    font-size: 28px;
    line-height: 46px;
  }
</style>
</head>
<body>
<div class="card">
  <svg class="card__art" viewBox="0 0 870 702" role="img" aria-label="Abstract splash of red, yellow, white and blue paint bursting outward across the dark background">
    <defs>
      <radialGradient id="splash-core" cx="355" cy="365" r="460" gradientUnits="userSpaceOnUse">
        <stop offset="0" stop-color="var(--splash-red)"/>
        <stop offset="0.12" stop-color="var(--splash-yellow)" stop-opacity="0.9"/>
        <stop offset="0.3" stop-color="var(--splash-white)" stop-opacity="0.55"/>
        <stop offset="0.55" stop-color="var(--splash-blue)" stop-opacity="0.45"/>
        <stop offset="1" stop-color="var(--card-black)" stop-opacity="0"/>
      </radialGradient>
    </defs>
    <rect width="870" height="702" fill="url(#splash-core)"/>
  </svg>

  <h1 class="card__name"><span>DJ</span><span>Marcus Tevane</span></h1>

  <address class="card__contact">
    <span class="contact__phone">415.308.2741</span>
    <span class="contact__line">djmarcustevane@mixmail.net</span>
    <span class="contact__line">www.vowlisting.net/djmarcustevane</span>
  </address>
</div>
</body>
</html>
```